Flyer redesign

We need this flier {Seasonal Care back 2018} redesigned for our 2019 season. It is attached below. New design should look different from current design. Be creative yet still professional.

Requirements
Must have
• Designed in photoshop.
• Should have the same text as current design. Only is "2019" instead of 2018. We want a different look with same info to send our customers next year.
• size: standard letter paper 8.5" x 11"
Nice to have
• Can use optional images provided. Not required though. See our website for more photos. thornbrookmemorial.org. send message through briskdrafts if you want a specific photo.
Should not have
• Do not take current design and just change date or image. Make the design look different.

```html
<!DOCTYPE html>
<html lang="en">
<head>
<meta charset="utf-8">
<title>Gravesite Landscaping Packages 2019 – Thornbrook Memorial</title>
<link href="https://fonts.googleapis.com/css2?family=Oswald:wght@600;700&family=Open+Sans:wght@400;600;700&display=swap" rel="stylesheet">
<style>
  :root{
    --maroon:#7b1f30;
    --maroon-dark:#5a1522;
    --gold:#b8ad7c;
    --badge:#e0b21f;
    --panel:#d9d9db;
    --ink:#3a3a3a;
    --paper:#ffffff;
    --backdrop:#ebebeb;
  }
  *{box-sizing:border-box;margin:0;padding:0}
  html,body{width:1200px;height:1200px;overflow:hidden;background:var(--backdrop)}
  body{font-family:"Open Sans",Arial,sans-serif;color:var(--ink)}
  .flyer{position:absolute;left:175px;top:50px;width:850px;height:1100px;background:var(--paper);overflow:hidden;box-shadow:0 4px 18px rgba(0,0,0,.12)}
  .brand{position:absolute;left:40px;top:38px;display:flex;align-items:center;gap:10px;font-size:24px;font-weight:600;color:var(--maroon);letter-spacing:1px;font-variant:small-caps}
  .brand-dot{width:14px;height:14px;border-radius:50%;background:var(--maroon)}
  .photo{position:absolute;left:0;top:100px;width:850px;height:330px;
    background:linear-gradient(180deg,#4f7a38 0%,#6f9a4a 45%,#a9b79a 62%,#8fa870 78%,#b9bcb7 100%);
    clip-path:polygon(0 0,100% 0,100% 78%,55% 100%,0 80%)}
  .banner{position:absolute;left:560px;top:70px;width:250px;height:420px;background:var(--maroon);
    display:flex;flex-direction:column;align-items:center;padding-top:40px;
    clip-path:polygon(0 0,100% 0,100% 100%,10% 94%,0 94%)}
  .banner-fold{position:absolute;left:540px;top:70px;width:20px;height:40px;background:var(--maroon-dark);clip-path:polygon(100% 0,100% 100%,0 100%)}
  .banner h1{font-family:"Oswald",Impact,sans-serif;font-weight:700;color:#fff;text-align:center;font-size:44px;line-height:1.12}
  .banner .year{font-size:82px;margin-top:8px}
  .badge{position:absolute;z-index:3;left:690px;top:405px;width:118px;height:118px;border-radius:50%;background:var(--badge);
    border:3px dashed rgba(255,255,255,.7);outline:5px solid var(--badge);display:flex;align-items:center;justify-content:center;
    font-family:"Oswald",Impact,sans-serif;font-weight:700;color:#fff;font-size:22px;line-height:1;text-align:center;transform:rotate(-20deg)}
  .side{position:absolute;left:560px;top:500px;width:250px;height:600px;background:var(--panel);padding:48px 18px 0 22px;text-align:right}
  h2{font-family:"Oswald",Impact,sans-serif;font-weight:700;color:var(--maroon);font-size:28px;line-height:1}
  .side h2{font-size:22px}
  .sub{font-size:11px;text-transform:uppercase;color:#555;margin-top:4px;line-height:1.4}
  ul{list-style:none;margin-top:10px}
  li{position:relative;font-size:16px;line-height:1.35;margin-bottom:6px}
  .side li{font-size:16px;margin-bottom:12px}
  .side li::before{content:"";display:inline-block;width:9px;height:9px;background:var(--maroon);margin-right:7px;vertical-align:1px}
  .main{position:absolute;left:70px;width:460px}
  .main li{padding-left:22px;text-align:justify}
  .main li::before{content:"";position:absolute;left:0;top:7px;width:9px;height:9px;background:var(--maroon)}
  .seasonal{top:470px}
  .endow{top:718px}
  .rates{display:flex;background:var(--gold);margin-top:12px;padding:10px 14px}
  .rate{flex:1;border-right:1px solid rgba(255,255,255,.5);padding-left:6px}
  .rate:last-child{border:none}
  .rate span{display:block;font-size:14px;color:#4a3a2a}
  .rate b{font-size:36px;font-weight:700;color:var(--maroon);line-height:1.05}
  .note{font-size:12px;text-align:right;margin-top:4px}
  .pay{display:flex;align-items:center;gap:20px;background:var(--gold);margin-top:10px;padding:8px 20px}
  .pay span{font-size:13px;text-transform:uppercase;color:#4a3a2a;line-height:1.2}
  .pay b{font-size:36px;color:var(--maroon)}
  .pay-notes{display:flex;justify-content:space-between;align-items:flex-start;gap:10px;margin-top:4px}
  .pay-notes .note{margin-top:0;white-space:nowrap;font-size:11px}
  .side .pay{background:var(--maroon);margin:6px -18px 0 -22px;padding:10px 14px;gap:14px}
  .side .pay span{color:#e8c9cf;font-size:11px}
  .side .pay b{color:#fff;font-size:32px}
  .fine{font-size:13px;line-height:1.35}
  .side .fine{margin-top:6px}
  .contact{position:absolute;left:70px;top:1030px}
  .phone{font-weight:700;font-style:italic;color:var(--maroon);font-size:28px;line-height:1.1}
  .web{font-size:15px;color:#555;margin-top:2px}
</style>
</head>
<body>
<article class="flyer">
  <div class="brand"><span class="brand-dot"></span>Thornbrook Memorial</div>
  <div class="photo" role="img" aria-label="Photo of a leafy cemetery path lined with headstones and trimmed hedges"></div>
  <div class="banner-fold"></div>
  <div class="banner"><h1>Gravesite<br>Landscaping<br>Packages<br><span class="year">2019</span></h1></div>

  <section class="main seasonal">
    <h2>SEASONAL CARE</h2>
    <p class="sub">Seasonal lansdcaping grave cars</p>
    <ul><li>Weeding and trimming services on your gravesite approximately every 7 weeks during the growing season: mid-April through mid-October</li></ul>
    <div class="rates">
      <div class="rate"><span>3 YEARS</span><b>$327</b></div>
      <div class="rate"><span>2 YEARS</span><b>$218</b></div>
      <div class="rate"><span>1 YEARS</span><b>$109</b></div>
    </div>
    <p class="note">Multi-year payment locks in current rates.</p>
  </section>

  <section class="main endow">
    <h2>BASIC CARE ENDOWMENT</h2>
    <p class="sub">Lansdcaping care forever for graves with no plantings</p>
    <ul>
      <li>Weeding and trimming services on your gravesite 2 times per year: mid-May and mid-September</li>
      <li>Monument leveling</li>
      <li>Payment ensures grave care forever</li>
    </ul>
    <div class="pay"><span>12 monthly<br>payments of</span><b>$280.42</b></div>
    <div class="pay-notes">
      <p class="fine">Call for the monument types d single<br>payment discount. Valid through 10/31/19.</p>
      <p class="note">*gravesites with single headstones.</p>
    </div>
  </section>

  <aside class="side">
    <h2>PERPETUAL CARE</h2>
    <p class="sub">Lansdcaping care forever for<br>graves with lantings</p>
    <ul>
      <li>Weeding and trimming services on your gravesite approximately every 7 weeks during the growing season: mid-April through mid-October</li>
      <li>Monument leveling and cleaning</li>
      <li>Payment ensures grave care forever</li>
      <li>Full bed of boxwood shrubs</li>
      <li>Replacement of shrubs</li>
      <li>Trust certificate</li>
    </ul>
    <div class="pay"><span>12 monthly<br>payments of</span><b>$280.42</b></div>
    <p class="fine">Call for single payment discount.<br>Valid through 10/31/19</p>
  </aside>

  <div class="badge">MOST<br>POPULAR</div>

  <footer class="contact">
    <p class="phone">(555) 214-3870</p>
    <p class="web">info@thornbrookmemorial.org | www.thornbrookmemorial.org</p>
  </footer>
</article>
</body>
</html>
```